Boom Way Hoist Service Business Cards

I need a business card for "Boom Way Hoist and Haulage"

Boomway2023@hoistmail.net

Hoist Works LLC, Boom Way Hoist and Haulage LLC

555.014.7260 | www.BOOMWAYHOISTS.example

Central Indiana & Northeast Ohio

(IN) 14820 Maple Lane Noblesville, IN 46000

(OH) 2450 Pell Street Akron, Ohio 44300

Colors
0094D4
00A9DD
6FCCEA
C7EBF8
E9F6FB
59FF00
82FF00
B8FF75
E3FFCB
F4FFEA
EE7325
F08F49
F5BC92
FAE3D3
FDF4ED
EB3D1F
EC4F4E
F09395
F8D3D4
FCEDEE
E54698
E96AAD
F1A4CE
F9D9EA
FCEFF6
A7469A
B969AE
D3A5CF
EDDBEB
F8F0F9

```html
<!DOCTYPE html>
<html lang="en">
<head>
<meta charset="utf-8">
<title>Boom Way Hoist and Haulage – Business Cards</title>
<link rel="stylesheet" href="https://fonts.googleapis.com/css2?family=Oswald:wght@500;600;700&family=Open+Sans:wght@400;600&display=swap">
<style>
  :root {
    --stage: #232323;
    --card: #29292d;
    --red: #eb3d1f;
    --green: #3fb54a;
    --white: #ffffff;
    --grey: #8a8a8a;
    --grey-dark: #4a4a4e;
  }
  * { box-sizing: border-box; margin: 0; padding: 0; }
  html, body {
    width: 1200px; height: 780px; overflow: hidden;
    background: var(--stage);
  }
  .canvas { position: relative; width: 1200px; height: 780px; }

  .card {
    position: absolute;
    width: 540px; height: 320px;
    background: var(--card);
    border: 3px solid var(--red);
    border-radius: 26px;
    overflow: hidden;
    box-shadow: 0 14px 30px rgba(0,0,0,.55);
  }
  .card--front { left: 40px; top: 60px; }
  .card--back { left: 620px; top: 400px; }

  /* Front */
  .brand {
    position: absolute; inset: 0;
    display: flex; align-items: center; justify-content: center; gap: 14px;
  }
  .brand__square { width: 22px; height: 22px; background: var(--red); }
  .brand__name {
    font-family: "Oswald", sans-serif; font-weight: 700;
    font-size: 34px; letter-spacing: .5px; text-transform: uppercase;
    color: var(--white);
  }

  /* Back */
  .accent-bar { position: absolute; right: 0; width: 26px; }
  .accent-bar--red { top: 0; height: 34px; background: var(--red); }
  .accent-bar--green { top: 34px; height: 34px; background: var(--green); }

  .details {
    position: absolute; right: 42px; top: 18px;
    text-align: right;
  }
  .company {
    font-family: "Oswald", sans-serif; font-weight: 700;
    font-size: 26px; line-height: 1.1; text-transform: uppercase;
  }
  .company--red { color: var(--red); }
  .company--green { color: var(--green); }
  .region {
    margin-top: 8px;
    font-family: "Oswald", sans-serif; font-weight: 600;
    font-size: 15px; color: var(--white);
  }
  .address {
    font-family: "Oswald", sans-serif; font-weight: 500;
    font-size: 14px; line-height: 1.35;
  }
  .address--in { color: var(--green); margin-top: 4px; }
  .address--oh { color: var(--red); }

  .contacts { margin-top: 12px; list-style: none; }
  .contacts li {
    display: flex; justify-content: flex-end; align-items: center; gap: 7px;
    font-family: "Open Sans", sans-serif; font-size: 13px; line-height: 1.45;
    color: var(--white);
  }
  .contacts svg { width: 12px; height: 12px; fill: var(--red); }

  .fleet-art {
    position: absolute; left: 26px; bottom: 18px;
    width: 210px; height: 190px;
    border-radius: 6px;
    background: linear-gradient(160deg, var(--grey-dark) 0%, var(--grey) 45%, var(--red) 75%, var(--green) 100%);
    opacity: .85;
  }
</style>
</head>
<body>
<main class="canvas">

  <section class="card card--front" aria-label="Business card front">
    <div class="brand">
      <span class="brand__square"></span>
      <span class="brand__name">Boom Way Hoist and Haulage</span>
    </div>
  </section>

  <section class="card card--back" aria-label="Business card back">
    <span class="accent-bar accent-bar--red"></span>
    <span class="accent-bar accent-bar--green"></span>

    <div class="fleet-art" role="img" aria-label="Illustration of a red concrete pump truck and a green mobile crane in front of a grey construction skyline"></div>

    <div class="details">
      <p class="company company--red">Hoist Works LLC</p>
      <p class="company company--green">Boom Way Hoist &amp; Haulage LLC</p>
      <p class="region">Central Indiana &amp; Northeast Ohio</p>
      <p class="address address--in">(IN) 14820 Maple Lane Noblesville, IN 46000</p>
      <p class="address address--oh">(OH) 2450 Pell Street Akron, Ohio 44300</p>
      <ul class="contacts">
        <li>555.014.7260
          <svg viewBox="0 0 24 24" aria-hidden="true"><path d="M6.6 10.8a15.5 15.5 0 0 0 6.6 6.6l2.2-2.2a1 1 0 0 1 1-.25 11.4 11.4 0 0 0 3.6.6 1 1 0 0 1 1 1V20a1 1 0 0 1-1 1A17 17 0 0 1 3 4a1 1 0 0 1 1-1h3.5a1 1 0 0 1 1 1c0 1.25.2 2.45.6 3.6a1 1 0 0 1-.25 1z"/></svg>
        </li>
        <li>www.boomwayhoists.example
          <svg viewBox="0 0 24 24" aria-hidden="true"><path d="M12 2a10 10 0 1 0 0 20 10 10 0 0 0 0-20zm6.9 6h-3a15.6 15.6 0 0 0-1.4-3.6A8 8 0 0 1 18.9 8zM12 4c.8 1.2 1.5 2.5 1.9 4h-3.8c.4-1.5 1.1-2.8 1.9-4zM4.3 14a8 8 0 0 1 0-4h3.4a16 16 0 0 0 0 4zm.8 2h3a15.6 15.6 0 0 0 1.4 3.6A8 8 0 0 1 5.1 16zm3-8h-3a8 8 0 0 1 4.4-3.6A15.6 15.6 0 0 0 8.1 8zM12 20c-.8-1.2-1.5-2.5-1.9-4h3.8c-.4 1.5-1.1 2.8-1.9 4zm2.3-6H9.7a14.7 14.7 0 0 1 0-4h4.6a14.7 14.7 0 0 1 0 4zm.2 5.6c.6-1.1 1.1-2.3 1.4-3.6h3a8 8 0 0 1-4.4 3.6zm1.8-5.6a16 16 0 0 0 0-4h3.4a8 8 0 0 1 0 4z"/></svg>
        </li>
        <li>Boomway2023@hoistmail.net
          <svg viewBox="0 0 24 24" aria-hidden="true"><path d="M3 5h18a1 1 0 0 1 1 1v12a1 1 0 0 1-1 1H3a1 1 0 0 1-1-1V6a1 1 0 0 1 1-1zm1 2.2V17h16V7.2l-8 5.3z M5.2 7 12 11.5 18.8 7z"/></svg>
        </li>
      </ul>
    </div>
  </section>

</main>
</body>
</html>
```